Best website on the WWW

I am looking to create a multi tab wesbite to revamp our outdated website.

Here is an example of a companies website I really like
https://ridgelinehaulers.example/

Target Market(s)

New customers, government agency's

Industry/Entity Type

Auto repair, towing and recovery, hazmat clean up

Coding

Coded - Design and coding required

Number of Pages Required

5+ page

Font styles to use
Sans Serif

Requirements
Nice to have
• I would like to see an interactive website, that includes details and photos from our companies

```html
<!DOCTYPE html>
<html lang="en">
<head>
<meta charset="utf-8">
<title>Ridgeline Spill Response</title>
<link rel="stylesheet" href="https://fonts.googleapis.com/css2?family=Rubik:wght@400;500;600;700&family=Michroma&display=swap">
<style>
:root{
  --red:#e3202b;
  --navy:#0b3079;
  --navy-deep:#0a2a66;
  --ink:#1b1b1b;
  --grey:#6d6d6d;
  --light:#f4f4f4;
  --dark:#141a24;
  --white:#ffffff;
}
*{margin:0;padding:0;box-sizing:border-box}
html,body{width:1200px;height:3780px;overflow:hidden}
body{position:relative;font-family:"Rubik",sans-serif;color:var(--ink);background:var(--white)}
.abs{position:absolute}
.btn{position:absolute;display:flex;align-items:center;justify-content:center;border-radius:26px;color:var(--white);font-weight:600;font-size:13px;letter-spacing:.2px;text-transform:uppercase}
.btn-red{background:var(--red)}
.btn-navy{background:var(--navy)}
.photo{position:absolute}
.section-title{position:absolute;left:0;width:1200px;text-align:center;font-family:"Michroma",sans-serif;font-size:33px;font-weight:400;color:var(--ink);text-transform:uppercase;letter-spacing:.5px}
.section-title span{color:var(--navy)}

/* header */
.brand{position:absolute;display:flex;align-items:center;gap:10px;font-family:"Rubik",sans-serif;font-weight:700;text-transform:uppercase}
.brand .mark{width:18px;height:18px;border-radius:50%;background:var(--red)}
.nav{position:absolute;left:416px;top:57px;display:flex;gap:20px;font-size:13px;font-weight:500;text-transform:uppercase}
.nav a{color:var(--ink);text-decoration:none}
.nav a.active{color:var(--red)}

/* hero */
.hero{position:absolute;left:0;top:128px;width:1200px;height:662px;background:linear-gradient(180deg,#6b6760 0%,#4c4843 45%,#3a3733 100%);overflow:hidden}
.hero h1{position:absolute;left:0;top:178px;width:1200px;text-align:center;color:var(--white);font-size:40px;line-height:50px;font-weight:600;text-transform:uppercase}
.chevron{position:absolute;left:568px;top:626px;width:64px;height:64px;border-radius:50%;background:var(--white);box-shadow:0 4px 12px rgba(0,0,0,.2);display:flex;align-items:center;justify-content:center}

/* about */
.about-frame{position:absolute;left:112px;top:830px;width:505px;height:385px;background:var(--white);box-shadow:0 0 10px rgba(0,0,0,.15);padding:8px}
.about-frame .photo{position:static;width:100%;height:100%;background:linear-gradient(160deg,#b9c8d6 0%,#8f9aa0 45%,#7c7b76 100%)}
.about h2{position:absolute;left:697px;top:880px;font-family:"Michroma",sans-serif;font-size:33px;font-weight:400}
.about h2 span{color:var(--navy)}
.about p{position:absolute;left:697px;top:948px;width:392px;font-size:13.5px;line-height:25px;color:var(--grey);text-align:justify}

/* services */
.services{position:absolute;left:0;top:1316px;width:1200px;height:592px;background:var(--light)}
.card{position:absolute;top:149px;width:312px;height:360px;overflow:hidden}
.card .label{position:absolute;left:0;bottom:22px;width:100%;text-align:center;color:var(--white);font-weight:600;font-size:17px;text-transform:uppercase}
.card-active{background:linear-gradient(180deg,#e42a31,#d41f28);color:var(--white);text-align:center}
.card-active h3{position:absolute;top:140px;width:100%;font-size:18px;font-weight:600;text-transform:uppercase}
.card-active p{position:absolute;top:175px;left:24px;width:264px;font-size:13px;line-height:25px}
.card-active .more{position:absolute;top:297px;width:100%;font-size:13px;font-weight:600;display:flex;justify-content:center;align-items:center;gap:6px}

/* features */
.features{position:absolute;left:0;top:1908px;width:1200px;height:700px;background:linear-gradient(180deg,#0b3179,#0a2d70)}
.features h2{position:absolute;left:0;top:70px;width:1155px;text-align:center;color:var(--white);font-family:"Michroma",sans-serif;font-size:25px;font-weight:400}
.hub{position:absolute;left:166px;top:266px;width:252px;height:252px;border-radius:50%;background:var(--white);display:flex;align-items:center;justify-content:center}
.feat-icon{position:absolute;left:535px;width:88px;height:88px;border-radius:50%;background:var(--white);border:6px solid #c5cbe0;display:flex;align-items:center;justify-content:center}
.feat{position:absolute;left:652px;width:382px;color:var(--white)}
.feat h3{font-size:16px;font-weight:600;text-transform:uppercase;margin-bottom:12px}
.feat p{font-size:11.5px;line-height:20.5px;text-align:justify}

/* gallery */
.tile{position:absolute}

/* footer */
.footer{position:absolute;left:0;top:3270px;width:1200px;height:510px;background:var(--dark);overflow:hidden}
.footer h4{position:absolute;color:var(--white);font-size:17px;font-weight:600;text-transform:uppercase}
.links{position:absolute;left:381px;top:252px;list-style:none;color:var(--white);font-size:14px}
.links li{height:39.5px;display:flex;gap:24px}
.links li::before{content:"»";color:var(--red);font-weight:700}
.contact{position:absolute;left:574px;color:var(--white);font-size:11.5px;line-height:20px}
.contact b{display:block;font-size:13.5px;font-weight:600;text-transform:uppercase}
.contact svg{position:absolute;left:0;top:3px}
.contact .txt{margin-left:34px}
.news{position:absolute;left:806px;top:252px;width:281px;height:48px;border-radius:24px;background:var(--white);border:2px solid var(--white)}
.news span{position:absolute;left:16px;top:14px;font-size:13px;color:var(--grey)}
.social{position:absolute;top:324px;width:44px;height:44px;border-radius:50%}
.copy{position:absolute;left:0;top:473px;width:1200px;text-align:center;color:var(--white);font-size:12px}
</style>
</head>
<body>

<!-- header -->
<header>
  <div class="brand" style="left:112px;top:48px;font-size:22px;color:var(--navy)"><span class="mark"></span>Ridgeline</div>
  <nav class="nav">
    <a class="active">Home</a><a>About Us</a><a>Our Services ⌄</a><a>Gallery</a><a>More ⌄</a>
  </nav>
  <div class="btn btn-navy" style="left:887px;top:40px;width:145px;height:50px">Get a Quote</div>
  <div class="abs" style="left:1039px;top:40px;width:50px;height:50px;border-radius:50%;background:var(--red);display:flex;align-items:center;justify-content:center">
    <svg width="26" height="26" viewBox="0 0 26 26"><circle cx="13" cy="13" r="10" fill="none" stroke="#fff" stroke-width="2"/><text x="13" y="17" text-anchor="middle" font-family="Rubik,sans-serif" font-size="10" font-weight="700" fill="#fff">24</text></svg>
  </div>
</header>

<!-- hero -->
<section class="hero">
  <div role="img" aria-label="Tow trucks and pickups parked in a yard with bare trees" class="photo" style="left:0;top:0;width:1200px;height:662px;background:linear-gradient(180deg,#7a756c 0%,#54504a 40%,#3d3a35 75%,#5c5045 100%)"></div>
  <h1>Towing, Auto and Truck<br>Repair. Family Owned</h1>
  <div class="btn btn-red" style="left:497px;top:305px;width:205px;height:48px">Shop Verified Reviews</div>
  <svg class="abs" style="left:0;top:0" width="1200" height="662" viewBox="0 0 1200 662">
    <path d="M0 662 Q600 440 1200 662 Z" fill="#0b3079"/>
    <path d="M0 662 Q600 470 1200 662 Z" fill="#fff"/>
  </svg>
  <div class="chevron" style="top:498px">
    <svg width="18" height="12" viewBox="0 0 18 12"><path d="M3 3 L9 9 L15 3" fill="none" stroke="#1b1b1b" stroke-width="2.4"/></svg>
  </div>
</section>

<!-- about -->
<section class="about">
  <div class="about-frame"><div role="img" aria-label="Red, white and blue tow truck parked beside a semi truck" class="photo"></div></div>
  <h2>About <span>Us</span></h2>
  <p>We now provide our customers with the ability to check their vehicle history on line! We will also send you email reminders when it is time to have your vehicle serviced according to your specific vehicle manufacture. Ask us how to get you registered today!</p>
  <div class="btn btn-red" style="left:697px;top:1110px;width:146px;height:49px">Learn More</div>
</section>

<!-- services -->
<section class="services">
  <h2 class="section-title" style="top:66px">Our <span>Services</span></h2>
  <div class="card" style="left:112px">
    <div role="img" aria-label="Flatbed tow truck carrying a pickup" class="photo" style="inset:0;background:linear-gradient(180deg,#8e959c,#5d6268 60%,#3d4045)"></div>
    <div class="label">Towing Services</div>
  </div>
  <div class="card card-active" style="left:444px">
    <svg class="abs" style="left:128px;top:52px" width="56" height="56" viewBox="0 0 56 56" fill="none" stroke="#fff" stroke-width="3">
      <circle cx="24" cy="30" r="14"/><circle cx="24" cy="30" r="5"/>
      <path d="M38 6 L38 24 M44 6 L44 50 M38 24 L44 24"/>
    </svg>
    <h3>Routine Service</h3>
    <p>Our services are vital in maintaining your fuel efficiency and increasing the overall lifespan of your vehicle. Book a service appointment today.</p>
    <div class="more">Learn More
      <svg width="13" height="13" viewBox="0 0 13 13"><circle cx="6.5" cy="6.5" r="6.5" fill="#fff"/><path d="M4.5 3.5 L7.5 6.5 L4.5 9.5" stroke="#e3202b" stroke-width="1.8" fill="none"/></svg>
    </div>
  </div>
  <div class="card" style="left:776px">
    <div role="img" aria-label="Open engine bay with timing chain exposed" class="photo" style="inset:0;background:linear-gradient(160deg,#6a5a4e,#3c3b3b 50%,#7b2a2e)"></div>
    <div class="label">Repairs</div>
  </div>
</section>

<!-- features -->
<section class="features">
  <div role="img" aria-label="Faint tow truck in the background" class="photo" style="left:480px;top:120px;width:720px;height:480px;background:radial-gradient(ellipse at 60% 55%,rgba(40,80,150,.45),rgba(11,49,121,0) 70%)"></div>
  <h2>Fast &amp; Friendly Customer Service</h2>
  <svg class="abs" style="left:0;top:0" width="1200" height="700" viewBox="0 0 1200 700" fill="none">
    <path d="M300 255 A156 156 0 0 1 300 530" stroke="#fff" stroke-width="2"/>
    <path d="M390 300 A150 150 0 0 1 390 510" stroke="#fff" stroke-width="2"/>
    <path d="M391 302 L458 210 L535 210 M447 393 L535 393 M391 509 L458 588 L535 588" stroke="#fff" stroke-width="1.5"/>
    <circle cx="391" cy="302" r="7" fill="#e3202b" stroke="#fff" stroke-width="2"/>
    <circle cx="447" cy="393" r="7" fill="#e3202b" stroke="#fff" stroke-width="2"/>
    <circle cx="391" cy="509" r="7" fill="#e3202b" stroke="#fff" stroke-width="2"/>
  </svg>
  <div class="hub"><div class="brand" style="position:static;font-size:24px;color:var(--navy)"><span class="mark"></span>Ridgeline</div></div>

  <div class="feat-icon" style="top:166px"><svg width="40" height="40" viewBox="0 0 40 40"><circle cx="20" cy="20" r="14" fill="none" stroke="#e3202b" stroke-width="5" stroke-dasharray="6 3"/><circle cx="20" cy="20" r="5" fill="#e3202b"/></svg></div>
  <div class="feat" style="top:164px"><h3>Experienced Technicians</h3><p>The mechanics at our shop have over 60 years of experience between them. They are dedicated to providing high-quality repairs to keep you safe and happy.</p></div>

  <div class="feat-icon" style="top:349px"><svg width="40" height="40" viewBox="0 0 40 40"><circle cx="20" cy="16" r="10" fill="#e3202b"/><path d="M6 30 Q20 22 34 30 L30 36 L10 36 Z" fill="#e3202b"/></svg></div>
  <div class="feat" style="top:337px"><h3>Competitive Pricing</h3><p>Whether you're coming in for a routine inspection or a repair service, we promise that you will be completely satisfied with our work. We provide 24-month warranties with most of our services for your peace of mind.</p></div>

  <div class="feat-icon" style="top:544px"><svg width="40" height="40" viewBox="0 0 40 40"><path d="M10 8 L30 8 L38 17 L20 36 L2 17 Z" fill="#e3202b"/><path d="M2 17 L38 17 M14 8 L20 36 L26 8" stroke="#fff" stroke-width="1.5" fill="none"/></svg></div>
  <div class="feat" style="top:531px"><h3>Our Quality Promise</h3><p>We're committed to providing a stress-free experience to both new and returning customers. Our shop only uses parts from reputable brands to ensure that your vehicle is always ready to drive.</p></div>
</section>

<!-- gallery -->
<section class="gallery">
  <h2 class="section-title" style="top:2696px">Our <span>Gallery</span></h2>
  <div role="img" aria-label="Engine cover close-up" class="tile" style="left:112px;top:2786px;width:234px;height:192px;background:linear-gradient(160deg,#4a4d52,#1f2124)"></div>
  <div role="img" aria-label="Black tow truck parked at a shop" class="tile" style="left:112px;top:2989px;width:234px;height:234px;background:linear-gradient(160deg,#9ea5aa,#2a2d2e 60%)"></div>
  <div role="img" aria-label="Black truck cab door with logo" class="tile" style="left:359px;top:2786px;width:235px;height:257px;background:linear-gradient(180deg,#55585a,#1e1f21)"></div>
  <div role="img" aria-label="Gear and transmission parts" class="tile" style="left:359px;top:3055px;width:235px;height:168px;background:linear-gradient(160deg,#cfd1d3,#6f7274)"></div>
  <div role="img" aria-label="Technician running diagnostics on a laptop" class="tile" style="left:607px;top:2786px;width:234px;height:165px;background:linear-gradient(160deg,#c8ced6,#4d5867)"></div>
  <div role="img" aria-label="Classic teal car on a flatbed" class="tile" style="left:607px;top:2963px;width:234px;height:260px;background:linear-gradient(180deg,#8fb3d6,#3f9c8a 50%,#3a3a3a)"></div>
  <div role="img" aria-label="Black metal equipment on asphalt" class="tile" style="left:855px;top:2786px;width:234px;height:257px;background:linear-gradient(180deg,#6b6b69,#454543)"></div>
  <div role="img" aria-label="Tow truck outside a red barn" class="tile" style="left:855px;top:3055px;width:234px;height:168px;background:linear-gradient(180deg,#b7c9d8,#6e7c5c 50%,#3c3d3a)"></div>
</section>

<!-- footer -->
<footer class="footer">
  <svg class="abs" style="left:0;top:0" width="1200" height="140" viewBox="0 0 1200 140">
    <rect width="1200" height="0" fill="#fff"/>
    <path d="M0 0 L1200 0 Q600 250 0 0 Z" fill="#0b3079"/>
    <path d="M0 0 L1200 0 Q600 222 0 0 Z" fill="#fff"/>
  </svg>
  <div class="brand" style="left:112px;top:318px;font-size:28px;color:var(--white)"><span class="mark" style="background:var(--white)"></span>Ridgeline</div>

  <h4 style="left:381px;top:212px">Quick Links</h4>
  <ul class="links"><li>Home</li><li>About Us</li><li>Services</li><li>Blogs</li><li style="font-weight:600">MORE</li></ul>

  <h4 style="left:574px;top:212px">Contact Info</h4>
  <div class="contact" style="top:252px">
    <svg width="12" height="14" viewBox="0 0 12 14"><path d="M6 0 A5 5 0 0 1 11 5 C11 9 6 14 6 14 C6 14 1 9 1 5 A5 5 0 0 1 6 0Z" fill="#e3202b"/><circle cx="6" cy="5" r="2" fill="#141a24"/></svg>
    <div class="txt"><b>Address:</b>2240 Valley Crest Rd, Millbrook,<br>OH, United States</div>
  </div>
  <div class="contact" style="top:330px">
    <svg width="14" height="14" viewBox="0 0 14 14"><path d="M3 1 L5 4 L4 6 Q6 9 8 10 L10 9 L13 11 L11 13 Q5 13 1 6 Q1 3 3 1Z" fill="#e3202b"/></svg>
    <div class="txt"><b>Phone:</b>+1 555-014-2290</div>
  </div>
  <div class="contact" style="top:385px">
    <svg width="14" height="11" viewBox="0 0 14 11"><rect width="14" height="11" fill="#e3202b"/><path d="M0 0 L7 6 L14 0" stroke="#141a24" stroke-width="1.4" fill="none"/></svg>
    <div class="txt"><b>Email:</b>service@ridgelinehaulers.example</div>
  </div>

  <h4 style="left:804px;top:212px">Newsletter Signup</h4>
  <div class="news"><span>Email Address</span>
    <div class="btn btn-red" style="right:2px;top:2px;width:94px;height:40px">Sign Up</div>
  </div>
  <div class="social" style="left:805px;background:var(--red)"></div>
  <div class="social" style="left:856px;background:var(--white)"></div>
  <div class="social" style="left:906px;background:var(--white)"></div>

  <div class="abs" style="left:112px;top:458px;width:976px;height:1px;background:rgba(255,255,255,.2)"></div>
  <div class="copy">© 2022 RIDGELINE SPILL RESPONSE &nbsp;|&nbsp; All Rights Reserved</div>
</footer>

</body>
</html>
```